Wren Vehicle Polishing (Mobile detail)

I need a business card made up. I'd like it to be different in some form, either raised, embossed, debossed, something cool that stands out. (preferably embossed text somewhere in it). I will be including the Initial png file. Let me know if you need the photoshop of adobe illustrator file to work with.

Information to be included: Text: XXX-XXX-XXXX Phone: XXX-XXX-XXXX Email: wrenpolishcrew@mailbox-demo.net Website: www.socialpage-demo.net/wrenpolishKTR Hours of operation: Mon - Fri 7:00AM to 8:00PM Sat - 10:00AM to 8:00PM

Target Market(s)

Mobile automotive detailing

Industry/Entity Type

Automotive

Contact Information for Business Card

Make it stand out with embossed lettering, I'd also like the background to be glossy black or matte, something that represents a shiny car, black preferred

Requirements
Must have
• A glossy background, or something.
• My logo, pick one of them that best fits your design.
Should not have
• White background,
• something that does not stand out.

```html
<!DOCTYPE html>
<html lang="en">
<head>
<meta charset="utf-8">
<title>Wren Vehicle Polishing – Business Card</title>
<link rel="stylesheet" href="https://fonts.googleapis.com/css2?family=Open+Sans:wght@400;600;700&display=swap">
<style>
  :root {
    --stage: #2b2c2f;
    --card-top: #1c1c1e;
    --card-bottom: #060607;
    --orange: #f37a21;
    --red: #e8412a;
    --white: #f4f4f4;
    --shadow: rgba(0, 0, 0, 0.55);
  }
  * { box-sizing: border-box; margin: 0; padding: 0; }
  html, body {
    width: 1200px;
    height: 864px;
    overflow: hidden;
    background: var(--stage);
    font-family: "Open Sans", Arial, sans-serif;
  }
  .stage {
    width: 1200px;
    height: 864px;
    display: flex;
    flex-direction: column;
    align-items: center;
    justify-content: center;
    gap: 56px;
  }
  .card {
    position: relative;
    width: 560px;
    height: 320px;
    border-radius: 3px;
    background: linear-gradient(160deg, var(--card-top) 0%, #0d0d0f 55%, var(--card-bottom) 100%);
    box-shadow: 0 14px 30px var(--shadow);
    overflow: hidden;
  }

  /* Front */
  .card-front {
    display: flex;
    align-items: center;
    justify-content: center;
  }
  .brand {
    display: flex;
    align-items: center;
    gap: 14px;
  }
  .brand-dot {
    width: 34px;
    height: 34px;
    border-radius: 50%;
    background: var(--orange);
  }
  .brand-name {
    color: var(--orange);
    font-weight: 700;
    font-size: 30px;
    letter-spacing: 0.5px;
  }

  /* Back */
  .card-back {
    text-align: center;
    color: var(--white);
  }
  .holder-name {
    margin-top: 28px;
    color: var(--orange);
    font-weight: 700;
    font-size: 20px;
    letter-spacing: 1.5px;
    text-transform: uppercase;
    line-height: 1.1;
  }
  .holder-title {
    font-size: 12px;
    font-weight: 400;
    line-height: 1.3;
  }
  .contact-list {
    display: grid;
    grid-template-columns: auto auto;
    justify-content: center;
    column-gap: 5px;
    margin-top: 20px;
    font-size: 13px;
    line-height: 20px;
  }
  .contact-label {
    color: var(--orange);
    font-weight: 700;
    text-align: right;
  }
  .contact-value {
    text-align: left;
  }
  .hours-heading {
    margin-top: 14px;
    color: var(--orange);
    font-weight: 700;
    font-size: 17px;
    letter-spacing: 0.5px;
    text-transform: uppercase;
  }
  .hours-list {
    margin-top: 6px;
    font-size: 14px;
    font-weight: 600;
    line-height: 21px;
  }
  .hours-day {
    color: var(--orange);
    font-weight: 700;
  }
  .accent-bands {
    position: absolute;
    left: 0;
    bottom: 26px;
    width: 560px;
    height: 20px;
  }
</style>
</head>
<body>
  <main class="stage">
    <section class="card card-front" aria-label="Card front">
      <div class="brand">
        <span class="brand-dot"></span>
        <span class="brand-name">Wren Vehicle Polishing</span>
      </div>
    </section>

    <section class="card card-back" aria-label="Card back">
      <h1 class="holder-name">Marcus Hale</h1>
      <p class="holder-title">Managing Director</p>

      <dl class="contact-list">
        <dt class="contact-label">Mobile:</dt><dd class="contact-value">XXX-XXX-XXXX</dd>
        <dt class="contact-label">Phone:</dt><dd class="contact-value">XXX-XXX-XXXX</dd>
        <dt class="contact-label">Email:</dt><dd class="contact-value">wrenpolishcrew@mailbox-demo.net</dd>
        <dt class="contact-label">Website:</dt><dd class="contact-value">www.socialpage-demo.net/wrenpolishKTR</dd>
      </dl>

      <h2 class="hours-heading">KTR Hours of Operation</h2>
      <div class="hours-list">
        <p><span class="hours-day">Mon - Fri:</span> 7:00AM to 8:00PM</p>
        <p><span class="hours-day">Sat:</span> 10:00AM to 8:00PM</p>
      </div>

      <svg class="accent-bands" viewBox="0 0 560 20" aria-hidden="true">
        <polygon points="0,0 290,0 282,20 0,20" fill="var(--orange)"/>
        <polygon points="300,0 560,0 560,20 292,20" fill="var(--red)"/>
      </svg>
    </section>
  </main>
</body>
</html>
```